Brisk Hollow Builders Needs A Flyer

We need a flyer for our newest product "The Cedarlane Garden Workroom"

Here is some copy for the flyer:

1. More and more people everyday are working from home and finding it difficult to disconnect from home activities in order to focus on their work. They are also finding it very expensive to add on to their existing house for a quiet place. Our archatectually stunning, Cedarlane Garden Workroom is the answer. The office studio measures 16' wide and 10' deep. 160 Square feet of space.

Perfect for dozens of purposes. Home office, design studio, artist studio, home school office, reading room, craft studio, drafting room.

Features include:

- Steel Framing. 40-60% lighter then wood, higher strength to weight ratio, resistant to mold and fire and steel is the most recycled material on earth!
- Spray foam insulation. Cool in the summer and warm in the winter.
- HVAC Mini Split with wireless remote control and thermostat.
- 100% Off grid with enough solar and battery storage to run your entire office. No need to pay for an expensive electric installation.
- Flush fitting floor outlets to reduce wires.
- TV mount (Optional with pre-wired electric, HDMI, digital audio & Cat 6)
- Windows are tempered glass custom made by Morvik Glazing.
- Solar qualifies for a 26% tax credit. This is not a write-off rather it is a direct reduction on your tax obligation.
- Thousands of dollars less than adding onto your home.
- Custom color, siding, features available.

This beautiful back yard office is delivered 100% assembled and ready to enjoy on the day of delivery.

We ship nationwide from our factory in South Carolina. Give us a call anytime to speak to a designer and start your dream office today!

555-318-4027
info@BriskHollowBuilders.example

```html
<!DOCTYPE html>
<html lang="en">
<head>
<meta charset="utf-8">
<title>Brisk Hollow Builders — The Cedarlane Garden Workroom</title>
<link rel="stylesheet" href="https://fonts.googleapis.com/css2?family=Barlow:wght@500;600;700;800&family=Barlow+Condensed:wght@700;800&family=Barlow+Semi+Condensed:wght@800&display=swap">
<style>
  :root {
    --orange: #e9a22c;
    --orange-soft: #f6d494;
    --green: #5aac4c;
    --green-dark: #3f8f38;
    --white: #ffffff;
    --ink: #222222;
    --paper: #f4f4f4;
    --photo-sky: #a9cde8;
    --photo-house: #4a4d4f;
    --photo-lawn: #6f9b45;
  }
  * { box-sizing: border-box; margin: 0; padding: 0; }
  html, body { width: 990px; height: 1200px; overflow: hidden; background: var(--white); }
  .flyer {
    position: relative; width: 990px; height: 1200px; overflow: hidden;
    background: linear-gradient(180deg, var(--white) 0%, var(--paper) 60%, #ececec 100%);
    font-family: "Barlow", sans-serif; color: var(--ink);
  }
  .shapes { position: absolute; inset: 0; }
  .photo-hero {
    position: absolute; left: 410px; top: 136px; width: 580px; height: 440px;
    clip-path: polygon(138px 0, 580px 0, 580px 440px, 230px 440px, 10px 120px);
    background: linear-gradient(180deg, var(--photo-sky) 0%, #dfeaf1 30%, var(--photo-house) 45%, #8a7a62 70%, var(--photo-lawn) 88%, #557c34 100%);
  }
  .brand {
    position: absolute; left: 110px; top: 120px; width: 300px; text-align: center;
    font-family: "Barlow", sans-serif; font-weight: 800; font-size: 34px; line-height: 1.05;
    color: var(--orange); text-transform: uppercase; letter-spacing: 1px;
  }
  .phone {
    position: absolute; left: 548px; top: 66px; display: flex; align-items: center; gap: 14px;
    font-family: "Barlow Semi Condensed", sans-serif; font-weight: 800; font-size: 42px; color: var(--white);
  }
  .phone svg { width: 40px; height: 40px; }
  .headline { position: absolute; left: 58px; top: 292px; }
  .headline-tag {
    display: inline-block; height: 67px; padding: 0 58px 0 26px; line-height: 67px;
    background: var(--green); clip-path: polygon(0 0, 88% 0, 100% 100%, 0 100%);
    font-family: "Barlow Condensed", sans-serif; font-weight: 800; font-size: 46px;
    letter-spacing: 9px; color: var(--white);
  }
  .headline-main {
    font-family: "Barlow Condensed", sans-serif; font-weight: 800; color: var(--white);
    text-transform: uppercase; line-height: 1; text-shadow: 2px 2px 0 #c98412;
  }
  .headline-main.big { font-size: 96px; margin-top: 8px; letter-spacing: 1px; }
  .headline-main.mid { font-size: 62px; margin-top: 6px; }
  .features {
    position: absolute; left: 58px; top: 584px; width: 560px; list-style: none;
    font-size: 14.5px; font-weight: 500; line-height: 19px;
  }
  .features li { position: relative; padding-left: 28px; margin-bottom: 7px; }
  .features li svg { position: absolute; left: 0; top: 1px; width: 17px; height: 17px; }
  .gallery-frame { position: absolute; border: 5px solid var(--orange); background: var(--white); }
  .gallery-frame .shot { width: 100%; height: 100%; }
  .frame-main { left: 627px; top: 608px; width: 304px; height: 177px; }
  .frame-main .shot { background: linear-gradient(180deg, #8fb56d 0%, #3e4345 35%, #50555a 70%, #5f8d3a 100%); }
  .frame-left { left: 627px; top: 795px; width: 146px; height: 136px; }
  .frame-left .shot { background: radial-gradient(ellipse at 50% 55%, #4c5053 0%, #8f8f8f 45%, #ffffff 75%); }
  .frame-right { left: 786px; top: 795px; width: 145px; height: 136px; }
  .frame-right .shot { background: radial-gradient(ellipse at 50% 55%, #9a9a9a 0%, #d6d6d6 45%, #ffffff 75%); }
  .contact { position: absolute; left: 58px; top: 1090px; list-style: none; }
  .contact li {
    display: flex; align-items: center; gap: 12px; margin-bottom: 12px;
    font-weight: 700; font-size: 21px; color: var(--white);
  }
  .contact svg { width: 18px; height: 18px; }
  .promo { position: absolute; left: 545px; top: 978px; width: 390px; text-align: center; color: var(--white); }
  .promo-lead { font-weight: 700; font-size: 17px; line-height: 23px; }
  .promo-rule { width: 120px; height: 2px; background: var(--white); margin: 14px auto 18px; }
  .promo-note { font-weight: 700; font-size: 13.5px; line-height: 20px; }
</style>
</head>
<body>
<div class="flyer">
  <div class="photo-hero" role="img" aria-label="Photo of a modern dark-sided garden office with large glass doors, furnished interior and lawn with stepping stones"></div>

  <svg class="shapes" viewBox="0 0 990 1200" aria-hidden="true">
    <defs>
      <linearGradient id="corner" x1="0" y1="0" x2="1" y2="1">
        <stop offset="0" stop-color="var(--orange)"/>
        <stop offset="1" stop-color="var(--orange-soft)" stop-opacity="0.2"/>
      </linearGradient>
    </defs>
    <polygon points="0,0 112,0 0,165" fill="url(#corner)"/>
    <rect x="0" y="0" width="440" height="9" fill="var(--orange)" opacity="0.8"/>
    <polygon points="443,0 990,0 990,136 548,136" fill="var(--green)"/>
    <polygon points="420,0 443,0 548,136 525,136" fill="var(--orange)"/>
    <polygon points="0,256 452,256 645,545 0,545" fill="var(--orange)"/>
    <polygon points="640,567 990,567 990,577 646,577" fill="var(--green)"/>
    <polygon points="538,958 990,958 990,1200 554,1200 483,1054" fill="var(--green)"/>
    <polygon points="0,1054 468,1054 548,1200 0,1200" fill="var(--orange)"/>
    <polygon points="468,1054 483,1054 554,1200 548,1200" fill="#c9e4c1"/>
  </svg>

  <div class="brand">Brisk Hollow<br>Builders</div>

  <div class="phone">
    <svg viewBox="0 0 40 40" aria-hidden="true">
      <circle cx="20" cy="20" r="18" fill="var(--white)"/>
      <circle cx="20" cy="20" r="14" fill="var(--orange)"/>
      <path d="M15 12c1-1 2-1 3 0l2 3c.5 1 0 2-1 2.5l-1 .5c.8 2 2.3 3.5 4.3 4.3l.5-1c.5-1 1.5-1.5 2.5-1l3 2c1 1 1 2 0 3l-1.3 1.3c-1.5 1.5-6 0-9.7-3.7S12.2 14.7 13.7 13.2z" fill="var(--white)"/>
    </svg>
    <span>555-318-4027</span>
  </div>

  <div class="headline">
    <div class="headline-tag">THE CEDARLANE</div>
    <div class="headline-main big">Garden</div>
    <div class="headline-main mid">Workroom</div>
  </div>

  <ul class="features">
    <li><svg viewBox="0 0 18 18"><circle cx="9" cy="9" r="8" fill="none" stroke="var(--green)" stroke-width="1.4"/><path d="M5.3 9.2l2.4 2.4 5-5" fill="none" stroke="var(--green)" stroke-width="1.5"/></svg>Steel Framing. 40-60% lighter then wood, higher strength to weight ratio, resistant to mold and fire and steel is the most recycled material on earth!</li>
    <li><svg viewBox="0 0 18 18"><circle cx="9" cy="9" r="8" fill="none" stroke="var(--green)" stroke-width="1.4"/><path d="M5.3 9.2l2.4 2.4 5-5" fill="none" stroke="var(--green)" stroke-width="1.5"/></svg>Spray foam insulation. Cool in the summer and warm in the winter.</li>
    <li><svg viewBox="0 0 18 18"><circle cx="9" cy="9" r="8" fill="none" stroke="var(--green)" stroke-width="1.4"/><path d="M5.3 9.2l2.4 2.4 5-5" fill="none" stroke="var(--green)" stroke-width="1.5"/></svg>HVAC Mini Split with wireless remote control and thermostat.</li>
    <li><svg viewBox="0 0 18 18"><circle cx="9" cy="9" r="8" fill="none" stroke="var(--green)" stroke-width="1.4"/><path d="M5.3 9.2l2.4 2.4 5-5" fill="none" stroke="var(--green)" stroke-width="1.5"/></svg>100% Off grid with enough solar and battery storage to<br>run your entire office. No need to pay for an expensive electric installation.</li>
    <li><svg viewBox="0 0 18 18"><circle cx="9" cy="9" r="8" fill="none" stroke="var(--green)" stroke-width="1.4"/><path d="M5.3 9.2l2.4 2.4 5-5" fill="none" stroke="var(--green)" stroke-width="1.5"/></svg>Flush fitting floor outlets to reduce wires.</li>
    <li><svg viewBox="0 0 18 18"><circle cx="9" cy="9" r="8" fill="none" stroke="var(--green)" stroke-width="1.4"/><path d="M5.3 9.2l2.4 2.4 5-5" fill="none" stroke="var(--green)" stroke-width="1.5"/></svg>TV mount (Optional with pre-wired electric, HDMI,<br>digital audio &amp; Cat 6)</li>
    <li><svg viewBox="0 0 18 18"><circle cx="9" cy="9" r="8" fill="none" stroke="var(--green)" stroke-width="1.4"/><path d="M5.3 9.2l2.4 2.4 5-5" fill="none" stroke="var(--green)" stroke-width="1.5"/></svg>Windows are tempered glass custom made by Morvik Glazing.</li>
    <li><svg viewBox="0 0 18 18"><circle cx="9" cy="9" r="8" fill="none" stroke="var(--green)" stroke-width="1.4"/><path d="M5.3 9.2l2.4 2.4 5-5" fill="none" stroke="var(--green)" stroke-width="1.5"/></svg>Solar qualifies for a 26% tax credit. This is not a write-off rather it is a direct reduction on your tax obligation.</li>
    <li><svg viewBox="0 0 18 18"><circle cx="9" cy="9" r="8" fill="none" stroke="var(--green)" stroke-width="1.4"/><path d="M5.3 9.2l2.4 2.4 5-5" fill="none" stroke="var(--green)" stroke-width="1.5"/></svg>Thousands of dollars less than adding onto your home.</li>
    <li><svg viewBox="0 0 18 18"><circle cx="9" cy="9" r="8" fill="none" stroke="var(--green)" stroke-width="1.4"/><path d="M5.3 9.2l2.4 2.4 5-5" fill="none" stroke="var(--green)" stroke-width="1.5"/></svg>Custom color, siding, features available.</li>
  </ul>

  <div class="gallery-frame frame-main"><div class="shot" role="img" aria-label="Rear view of the garden office with solar panels on its roof, set in a planted garden"></div></div>
  <div class="gallery-frame frame-left"><div class="shot" role="img" aria-label="Rendering of the garden office exterior on a white background"></div></div>
  <div class="gallery-frame frame-right"><div class="shot" role="img" aria-label="Drawing of the steel frame structure of the garden office"></div></div>

  <ul class="contact">
    <li><svg viewBox="0 0 18 18" aria-hidden="true"><rect x="1.5" y="3.5" width="15" height="11" fill="none" stroke="var(--white)" stroke-width="1.3"/><path d="M1.5 3.5l7.5 6 7.5-6" fill="none" stroke="var(--white)" stroke-width="1.3"/></svg>info@BriskHollowBuilders.example</li>
    <li><svg viewBox="0 0 18 18" aria-hidden="true"><circle cx="9" cy="9" r="7.5" fill="none" stroke="var(--white)" stroke-width="1.3"/><ellipse cx="9" cy="9" rx="3.5" ry="7.5" fill="none" stroke="var(--white)" stroke-width="1.2"/><path d="M1.5 9h15M3 5h12M3 13h12" stroke="var(--white)" stroke-width="1.1"/></svg>www.BriskHollowBuilders.example</li>
  </ul>

  <div class="promo">
    <p class="promo-lead">This Beautiful Back Yard Office is Delivered 100% Assembled and Ready to Enjoy on the day of Delivery.</p>
    <div class="promo-rule"></div>
    <p class="promo-note">We ship nationwide from our factory in South Carolina. Give us a call anytime to speak to a designer and start your dream office today!</p>
  </div>
</div>
</body>
</html>
```